Homepage web design

I need a homepage design that will be easy to build into a default Word Press theme. Basically, header, navigation, body with sidebar, and footer.

This website is for a small commercial real estate firm in the Washington DC, Maryland and Virginia market.

THIS IS NOT A HOUSING/RESIDENTIAL WEBSITE. PLEASE DO NOT ADD ANY PROPERTY SEARCH FUNCTIONALITY.

Target Market(s)

People looking for basic information about the team and services provided.

Industry/Entity Type

Real Estate

Requirements
Must have
• Professional look. Clean design.

```html
<!DOCTYPE html>
<html lang="en">
<head>
<meta charset="utf-8">
<title>Capitol Realty Partners — Home</title>
<link rel="stylesheet" href="https://fonts.googleapis.com/css2?family=Questrial&family=Arimo:wght@400;700&display=swap">
<style>
  :root {
    --orange: #ff8f1c;
    --orange-light: #ffad55;
    --orange-deep: #f7830f;
    --ink: #111111;
    --body-ink: #333333;
    --rule: #e2e2e2;
    --slider-bg: #eef2f7;
    --chevron: #c7d3e1;
    --white: #ffffff;
    --frame: #a9a9a9;
  }
  * { margin: 0; padding: 0; box-sizing: border-box; }
  html, body { width: 1200px; height: 1000px; overflow: hidden; background: var(--white); }
  body { position: relative; font-family: "Questrial", sans-serif; color: var(--ink); }

  .site-header {
    position: absolute; left: 0; top: 0; width: 1200px; height: 58px;
    background: linear-gradient(180deg, var(--orange-deep) 0%, var(--orange) 55%, var(--orange-light) 100%);
    overflow: hidden;
  }
  .site-header .sheen {
    position: absolute; left: 0; top: 0; width: 1200px; height: 58px;
  }
  .brand {
    position: absolute; left: 160px; top: 0; width: 110px; height: 58px;
    background: var(--white);
    display: flex; align-items: center; justify-content: center; gap: 5px;
  }
  .brand-mark { width: 8px; height: 8px; background: #1f8a4c; border-radius: 50%; }
  .brand-name {
    font-family: "Questrial", sans-serif; font-size: 13px; line-height: 1.05;
    color: #1f8a4c; text-align: left;
  }
  .main-nav { position: absolute; top: 12px; left: 0; width: 1200px; }
  .main-nav a {
    position: absolute; color: var(--white); text-decoration: none;
    font-size: 14px; letter-spacing: 0.6px; white-space: nowrap;
  }
  .main-nav a.is-current { text-shadow: 0 0 6px rgba(255,255,255,0.9); }

  .hero {
    position: absolute; left: 233px; top: 76px; width: 734px; height: 177px;
    background: var(--slider-bg);
  }
  .hero-photo {
    position: absolute; left: 39px; top: 0; width: 657px; height: 182px;
    background: linear-gradient(180deg, #c9c4c6 0%, #9a8f86 45%, #5d5750 75%, #4a4a40 100%);
    box-shadow: 0 6px 8px rgba(0,0,0,0.25);
  }
  .hero-bar {
    position: absolute; left: 39px; top: 179px; width: 657px; height: 8px;
    background: var(--orange);
  }
  .hero-arrow { position: absolute; top: 68px; width: 24px; height: 24px; }
  .hero-arrow.prev { left: 8px; }
  .hero-arrow.next { left: 703px; }
  .hero-dots { position: absolute; left: 614px; top: 167px; display: flex; gap: 6px; }
  .hero-dots span { width: 10px; height: 10px; border-radius: 50%; background: #dfe6ee; }
  .hero-dots span.active { background: #6f7f91; }

  .tagline {
    position: absolute; left: 330px; top: 279px; width: 540px;
    text-align: center; font-size: 13px; line-height: 12px; letter-spacing: 0.5px;
  }

  .section-head { position: absolute; left: 188px; width: 823px; height: 28px; }
  .section-head::before {
    content: ""; position: absolute; left: 0; right: 0; top: 13px; height: 2px; background: var(--rule);
  }
  .section-head h2 {
    position: absolute; left: 279px; top: 0; width: 264px; height: 28px;
    background: var(--orange); border: 1px solid #d77a1a; border-radius: 2px;
    color: var(--white); font-family: "Arimo", sans-serif; font-weight: 400;
    font-size: 14px; letter-spacing: 0.8px; line-height: 26px; text-align: center;
  }

  .divider { position: absolute; left: 188px; width: 823px; height: 2px; background: var(--rule); }

  .service { position: absolute; width: 345px; }
  .service svg { position: absolute; left: -43px; top: 2px; width: 22px; height: 22px; }
  .service h3 {
    font-family: "Arimo", sans-serif; font-weight: 400; font-size: 13.5px;
    letter-spacing: 0.6px; color: var(--ink); margin-bottom: 6px;
  }
  .service p { font-size: 9px; line-height: 12.8px; letter-spacing: 0.7px; color: var(--body-ink); }

  .product-frame {
    position: absolute; border: 1px solid var(--frame); background: var(--white); padding: 5px;
  }
  .product-frame .photo { width: 100%; height: 100%; }
  .product-caption {
    position: absolute; font-family: "Arimo", sans-serif; font-weight: 700;
    font-size: 7.4px; line-height: 12.4px; letter-spacing: 0.4px; color: var(--ink);
  }

  .site-footer {
    position: absolute; left: 0; top: 963px; width: 1200px; height: 37px; background: var(--orange);
  }
  .site-footer p {
    position: absolute; left: 101px; top: 14px; color: var(--white);
    font-size: 9.5px; letter-spacing: 0.8px; word-spacing: 1px;
  }
</style>
</head>
<body>

<header class="site-header">
  <svg class="sheen" viewBox="0 0 1200 58" aria-hidden="true">
    <path d="M270 40 C 520 20, 760 70, 1200 28 L1200 58 L270 58 Z" fill="#ffc27e" opacity="0.45"/>
  </svg>
  <div class="brand">
    <span class="brand-mark"></span>
    <span class="brand-name">Capitol Realty<br>Partners</span>
  </div>
  <nav class="main-nav">
    <a class="is-current" style="left:513px">HOME</a>
    <a style="left:617px">ABOUT</a>
    <a style="left:725px">SERVICES</a>
    <a style="left:852px">GALLERY</a>
    <a style="left:973px">CONTACTS</a>
  </nav>
</header>

<section class="hero">
  <div class="hero-photo" role="img" aria-label="Photograph of a large stone house with garages and autumn trees"></div>
  <div class="hero-bar"></div>
  <svg class="hero-arrow prev" viewBox="0 0 24 24" aria-hidden="true"><path d="M17 2 L5 12 L17 22" fill="none" stroke="var(--chevron)" stroke-width="4"/></svg>
  <svg class="hero-arrow next" viewBox="0 0 24 24" aria-hidden="true"><path d="M7 2 L19 12 L7 22" fill="none" stroke="var(--chevron)" stroke-width="4"/></svg>
  <div class="hero-dots"><span></span><span></span><span class="active"></span><span></span></div>
</section>

<p class="tagline">Lorem ipsum dolor sit amet, consectetur adipiscing elit. Aenean accumsan dapibus libero, id laoreet magna.</p>

<div class="section-head" style="top:311px"><h2>Our Main Services</h2></div>

<article class="service" style="left:221px;top:362px">
  <svg viewBox="0 0 24 24" aria-hidden="true"><path d="M12 3 L1 12 H4 V21 H10 V15 H14 V21 H20 V12 H23 Z" fill="var(--orange)"/></svg>
  <h3>Nunc ac tempor nunc</h3>
  <p>Sed venenatis, odio eget suscipit sagittis, magna nulla venenatis neque, non tempus metus lectus a eros. Fusce adipiscing aliquet purus, ut blandit nisi ultrices fringilla. Praesent posuere libero id justo lacinia accumsan.</p>
</article>
<article class="service" style="left:674px;top:362px">
  <svg viewBox="0 0 24 24" aria-hidden="true"><path d="M10 2 A7 7 0 0 1 17 9 C17 14 10 21 10 21 C10 21 3 14 3 9 A7 7 0 0 1 10 2 Z" fill="var(--orange)"/><circle cx="10" cy="9" r="3" fill="#fff"/><circle cx="19" cy="18" r="3.5" fill="none" stroke="var(--orange)" stroke-width="2"/></svg>
  <h3>Proin sed dignissim</h3>
  <p>Cras dictum, enim quis rutrum fringilla, quam mi egestas ipsum, vitae malesuada dui diam id sapien. Suspendisse porttitor ultricies nunc. Quisque orci erat, dapibus ultrices convallis sed, aliquet id nunc.</p>
</article>

<div class="divider" style="top:452px"></div>

<article class="service" style="left:221px;top:479px">
  <svg viewBox="0 0 24 24" aria-hidden="true"><path d="M1 7 H10 C11 7 12 8 12 9 C12 8 13 7 14 7 H23 V20 H14 C13 20 12 21 12 21 C12 21 11 20 10 20 H1 Z" fill="none" stroke="var(--orange)" stroke-width="2.2"/><path d="M12 9 V20" stroke="var(--orange)" stroke-width="2"/><path d="M18 2 L22 5" stroke="var(--orange)" stroke-width="2"/></svg>
  <h3>Curabitur interdum varius vehicula</h3>
  <p>Quisque orci erat, dapibus ultrices convallis sed, aliquet id nunc. Curabitur interdum varius vehicula. Donec suscipit dolor a libero aliquam, fermentum porttitor turpis interdum. Aenean pulvinar consequat elit, in sagittis lacus rutrum eu.</p>
</article>
<article class="service" style="left:674px;top:479px">
  <svg viewBox="0 0 24 24" aria-hidden="true"><rect x="2" y="4" width="20" height="17" fill="none" stroke="var(--orange)" stroke-width="2"/><rect x="2" y="4" width="20" height="4" fill="var(--orange)"/><path d="M6 12 H9 M11 12 H14 M16 12 H19 M6 16 H9 M11 16 H14 M16 16 H19" stroke="var(--orange)" stroke-width="2"/></svg>
  <h3>Vestibulum interdum nulla et</h3>
  <p>Donec porttitor metus eget turpis iaculis ullamcorper. Integer sit amet laoreet justo. Nunc viverra tempor elit in consectetur. Proin pulvinar tincidunt luctus. Vestibulum fermentum est est, non molestie justo lobortis eget.</p>
</article>

<div class="divider" style="top:576px"></div>

<article class="service" style="left:221px;top:603px">
  <svg viewBox="0 0 24 24" aria-hidden="true"><rect x="1" y="2" width="22" height="15" rx="1" fill="var(--orange)"/><rect x="3" y="4" width="18" height="11" fill="#fff"/><path d="M10 17 V21 H7 V23 H17 V21 H14 V17 Z" fill="var(--orange)"/></svg>
  <h3>Nulla quis purus auctor</h3>
  <p>Morbi tempor sollicitudin libero non rhoncus. Nam viverra semper metus, id malesuada elit aliquam at. Cum sociis natoque penatibus et magnis dis parturient montes, nascetur ridiculus mus. Maecenas scelerisque lacus vitae neque.</p>
</article>
<article class="service" style="left:674px;top:603px">
  <svg viewBox="0 0 24 24" aria-hidden="true"><circle cx="12" cy="12" r="11" fill="var(--orange)"/><path d="M6 6 C9 8 8 11 11 12 C13 13 11 16 13 18 M15 4 C16 7 19 8 21 10" fill="none" stroke="#fff" stroke-width="2"/></svg>
  <h3>Vestibulum interdum nulla et</h3>
  <p>Donec porttitor metus eget turpis iaculis ullamcorper. Integer sit amet laoreet justo. Nunc viverra tempor elit in consectetur. Proin pulvinar tincidunt luctus. Vestibulum fermentum est est, non molestie justo lobortis eget.</p>
</article>

<div class="section-head" style="top:700px"><h2>Features Products</h2></div>

<div class="product-frame" style="left:219px;top:746px;width:116px;height:62px">
  <div class="photo" role="img" aria-label="Greyscale photo of hands holding a small model house" style="background:linear-gradient(180deg,#e8e8e8,#a8a8a8 60%,#d0d0d0)"></div>
</div>
<p class="product-caption" style="left:221px;top:819px;width:170px">Lorem ipsum dolor sit amet, consectetur adipiscing elit. In ac felis quis nisi fringilla tristique nec non metus. Class aptent taciti sociosqu ad litora torquent per conubia nostra, per inceptos himenaeos.</p>

<div class="product-frame" style="left:509px;top:746px;width:141px;height:83px">
  <div class="photo" role="img" aria-label="Greyscale photo of a suburban street with houses" style="background:linear-gradient(180deg,#bdbdbd,#6e6e6e 55%,#9a9a9a)"></div>
</div>
<p class="product-caption" style="left:511px;top:839px;width:225px">Lorem ipsum dolor sit amet, consectetur adipiscing elit. In ac felis quis nisi fringilla tristique nec non metus. Class aptent taciti sociosqu ad litora torquent per conubia nostra, per inceptos himenaeos. Phasellus laoreet, urna non fringilla dignissim, arcu leo blandit risus, itae scelerisque sem.</p>

<div class="product-frame" style="left:801px;top:736px;width:122px;height:91px">
  <div class="photo" role="img" aria-label="Greyscale photo of hands holding a small model house" style="background:linear-gradient(180deg,#ececec,#a4a4a4 60%,#d4d4d4)"></div>
</div>
<p class="product-caption" style="left:803px;top:828px;width:170px">Lorem ipsum dolor sit amet, consectetur adipiscing elit. In ac felis quis nisi fringilla tristique nec non metus. Class aptent taciti sociosqu ad litora torquent per conubia nostra, per inceptos himenaeos.</p>

<footer class="site-footer">
  <p>REAL ESTATE ©2013 REALESTATE &nbsp; PRIVACY POLICY</p>
</footer>

</body>
</html>
```